Coral Bay Dental Surgery Business Cards

Hi there

Can i please have a simple business card designed (front and back with a black background) using out white reverse logo and the same font used for the logo?
On the back we can just have the logo. Full details at the front part.
Here are the details:

Name of the surgery: Coral Bay | Dental Surgery
Name on the business card: Dr Owen Thackery
Credentials:
BDSc (KTL)
MSc Oral Implantology (Halvorsen, Frankfurt)
Fellow & Diplomate (Meridian Council of Restorative Prosthetics)

Email: owen.thackery@coralbaysmile.example
Address: 17 Lisgrove Rd Karrinyup
Website: coralbaysmile.example
Phone: 1800 316 482

We have attached our high res logo and a rudimentary version of the business card which is not necessarily what we want but gives all the details
We would like to have the print ready version. Thanks.

Contact Information for Business Card

website. credentials. qr code. address. phone number

Requirements
Must have
• QR code

```html
<!DOCTYPE html>
<html lang="en">
<head>
<meta charset="utf-8">
<title>Coral Bay Dental Surgery – Business Cards</title>
<link href="https://fonts.googleapis.com/css2?family=Montserrat:wght@300;400;500;600;700&display=swap" rel="stylesheet">
<style>
  :root {
    --page: #f8f8f8;
    --card: #000000;
    --white: #ffffff;
    --light-text: #e6e6e6;
    --teal-name: #0e8fa8;
    --teal-rule: #19b4c2;
    --teal-icon: #2ec8bf;
    --faint: #2a2a2a;
    --qr-fill: #ffffff;
  }
  * { margin: 0; padding: 0; box-sizing: border-box; }
  html, body { width: 900px; height: 1200px; overflow: hidden; }
  body {
    background: var(--page);
    font-family: "Montserrat", sans-serif;
    position: relative;
  }
  .card {
    position: absolute;
    width: 466px;
    height: 266px;
    background: var(--card);
    overflow: hidden;
  }
  .card--logo { left: 226px; top: 226px; }
  .card--details { left: 229px; top: 535px; }

  .faint-mark {
    position: absolute;
    right: -60px;
    top: 30px;
    width: 170px;
    height: 170px;
    border-radius: 50%;
    background: var(--faint);
    opacity: 0.55;
  }

  .brand {
    position: absolute;
    left: 140px;
    top: 110px;
    display: flex;
    align-items: center;
    gap: 10px;
  }
  .brand__dot {
    width: 14px; height: 14px;
    border-radius: 50%;
    background: var(--white);
  }
  .brand__name {
    color: var(--white);
    font-weight: 600;
    font-size: 16px;
    letter-spacing: 0.5px;
  }

  .doctor {
    position: absolute;
    left: 35px;
    top: 40px;
  }
  .doctor__name {
    color: var(--teal-name);
    font-size: 22px;
    line-height: 26px;
    letter-spacing: 0.5px;
    white-space: nowrap;
    display: inline-block;
    border-bottom: 1.5px solid var(--teal-rule);
    padding-bottom: 2px;
  }
  .doctor__name strong { font-weight: 700; }
  .doctor__name span { font-weight: 300; }

  .credentials {
    margin-top: 4px;
    width: 302px;
    padding: 0 0 5px 2px;
    border-bottom: 1.5px solid var(--teal-rule);
    color: var(--light-text);
    font-size: 13px;
    line-height: 16.2px;
    font-weight: 300;
    white-space: nowrap;
  }
  .credentials b { font-weight: 600; color: var(--white); }

  .contacts {
    position: absolute;
    left: 37px;
    top: 164px;
    list-style: none;
  }
  .contacts li {
    display: flex;
    align-items: center;
    gap: 3px;
    height: 16px;
    color: var(--white);
    font-size: 13px;
    font-weight: 600;
    white-space: nowrap;
  }
  .contacts svg { width: 13px; height: 13px; flex: none; }

  .qr-code {
    position: absolute;
    left: 378px;
    top: 176px;
    width: 58px;
    height: 58px;
    background: var(--qr-fill);
    border-radius: 3px;
  }
</style>
</head>
<body>

  <section class="card card--logo" aria-label="Business card logo side">
    <div class="faint-mark" aria-hidden="true"></div>
    <div class="brand">
      <span class="brand__dot"></span>
      <span class="brand__name">Coral Bay | Dental Surgery</span>
    </div>
  </section>

  <section class="card card--details" aria-label="Business card details side">
    <div class="faint-mark" aria-hidden="true"></div>
    <div class="doctor">
      <h1 class="doctor__name"><strong>Dr OWEN</strong> <span>THACKERY</span></h1>
      <p class="credentials">
        BDSc <b>(KTL)</b><br>
        MSc Oral Implantology <b>(Halvorsen, Frankfurt)</b><br>
        Fellow &amp; Diplomate<br>
        <b>(Meridian Council of Restorative Prosthetics)</b>
      </p>
    </div>
    <ul class="contacts">
      <li>
        <svg viewBox="0 0 16 16" aria-hidden="true"><circle cx="8" cy="8" r="8" fill="#2ec8bf"/><rect x="4" y="5" width="8" height="6" fill="none" stroke="#000" stroke-width="1.1"/><path d="M4 5l4 3.5L12 5" fill="none" stroke="#000" stroke-width="1.1"/></svg>
        owen.thackery@coralbaysmile.example
      </li>
      <li>
        <svg viewBox="0 0 16 16" aria-hidden="true"><circle cx="8" cy="8" r="8" fill="#2ec8bf"/><path d="M8 13s-3.5-3.8-3.5-6.2a3.5 3.5 0 0 1 7 0C11.5 9.2 8 13 8 13z" fill="none" stroke="#000" stroke-width="1.2"/><circle cx="8" cy="6.8" r="1.2" fill="#000"/></svg>
        17 Lisgrove Rd Karrinyup
      </li>
      <li>
        <svg viewBox="0 0 16 16" aria-hidden="true"><circle cx="8" cy="8" r="8" fill="#2ec8bf"/><path d="M5.5 3.5v8.5l2.2-2 1.6 3 1.3-.7-1.6-2.9 2.9-.3z" fill="#000"/></svg>
        www.coralbaysmile.example
      </li>
      <li>
        <svg viewBox="0 0 16 16" aria-hidden="true"><circle cx="8" cy="8" r="8" fill="#2ec8bf"/><path d="M5.3 4c.4-.3.9-.2 1.1.2l.8 1.5c.2.4.1.8-.2 1l-.6.5c.5 1.1 1.3 1.9 2.4 2.4l.5-.6c.3-.3.7-.4 1-.2l1.5.8c.4.2.5.7.2 1.1l-.6.8c-.4.4-1 .6-1.6.4C7.5 11.2 4.8 8.5 4.1 6.2c-.2-.6 0-1.2.4-1.6z" fill="#000"/></svg>
        1800 316 482
      </li>
    </ul>
    <div class="qr-code" role="img" aria-label="QR code linking to the surgery website"></div>
  </section>

</body>
</html>
```